Occupational Therapy Needs an eye catching brochure for new business

I need a brochure for a new business that would be eye catching. I am an occupational therapist and this business will specifically deal with auditory processing delays and visual processing delays.If the childs delays stem from unintegrated reflexes that will be dealt with,as well. I have attached a brochure that I created. After having created it I decided that I wanted to seek professional graphics artist to help create an eye catching brochure that would attract more attention then my current unprofessional one. The attached brochures backgrounds should be changed. The wording should be changed and be more professionalized but the message should stay. I do not have a logo, since I am new, so you can create one for me, as well.

Please keep it a tri-fold. I have added the original brother file .edit and a word document with my text inside. Please give the brochure a professional look. I want those seeing my brochure to get the feel that my therapy business is a very professional and experienced business.Thank You Added Sunday, April 26, 2015

Parents of children with learning delays, whom are struggling and not getting good grades in school.

• Please keep it a tri-fold brochure
• Please include on the front page the following questions, they can be worded differently:
• Does your child have difficulty learning ABC and /or aleph bet?
• Does your child know the information for the test and does not do well on the test?
• Does your child have difficulty remembering name and dates in school, for test, or every day life?
• Please do not include pictures of Adults in the brochure.

```html
<!DOCTYPE html>
<html lang="en">
<head>
<meta charset="utf-8">
<title>Bright Steps – Tri-fold Brochure</title>
<link href="https://fonts.googleapis.com/css2?family=Roboto+Slab:wght@300;400;700&family=Montserrat:wght@600;700&family=Open+Sans:wght@400;600;700&display=swap" rel="stylesheet">
<style>
  :root {
    --bg: #8f8f8f;
    --paper: #f4f4f4;
    --blue: #2ea8dc;
    --green: #8cc63f;
    --green-light: #a6d454;
    --orange: #ef6a23;
    --ink: #333333;
    --white: #ffffff;
    --icon: #3b3b3b;
  }
  * { box-sizing: border-box; margin: 0; padding: 0; }
  html, body { width: 1200px; height: 845px; overflow: hidden; }
  body {
    background: radial-gradient(ellipse at center, #b0b0b0 0%, var(--bg) 100%);
    font-family: "Open Sans", sans-serif;
    color: var(--ink);
    position: relative;
  }
  .brochure {
    position: absolute; left: 60px; top: 42px;
    width: 1080px; height: 760px;
    display: flex;
    background: var(--paper);
    box-shadow: 0 10px 30px rgba(0,0,0,.35);
  }
  .panel {
    position: relative; width: 360px; height: 100%;
    overflow: hidden;
    border-right: 1px solid rgba(0,0,0,.06);
  }
  .panel:last-child { border-right: none; }

  /* Shared bands */
  .header-band {
    position: absolute; left: 0; top: 0; width: 100%; height: 90px;
    background: var(--blue);
  }
  .header-band.thin { height: 40px; }
  .brand {
    position: absolute; left: 28px; top: 24px;
    font-family: "Roboto Slab", serif; font-weight: 400;
    font-size: 32px; color: var(--white); letter-spacing: .5px;
  }
  .footer-band {
    position: absolute; left: 0; bottom: 0; width: 100%; height: 150px;
    background: linear-gradient(180deg, var(--green-light), var(--green));
    display: flex; align-items: center; justify-content: center;
    text-align: center; padding: 0 30px;
    font-family: "Montserrat", sans-serif; font-weight: 700;
    color: var(--white);
  }
  .footer-band.note { font-family: "Open Sans", sans-serif; font-size: 17px; line-height: 1.35; }
  .footer-band.claim { font-size: 21px; line-height: 1.3; }

  /* Contact panel */
  .contact { position: absolute; left: 0; top: 130px; width: 100%; text-align: center; }
  .contact-icon {
    width: 54px; height: 54px; border-radius: 50%;
    background: var(--icon); margin: 0 auto 10px;
    display: flex; align-items: center; justify-content: center;
    color: var(--white); font-size: 28px; font-weight: 700;
  }
  .contact-line { font-weight: 700; font-size: 17px; margin-bottom: 22px; }
  .contact-line.email { margin-bottom: 4px; }
  .contact-name { color: var(--blue); font-weight: 700; font-size: 17px; }
  .offer {
    position: absolute; left: 80px; top: 400px;
    width: 200px; height: 200px; border-radius: 50%;
    border: 7px solid var(--orange); background: var(--white);
    display: flex; flex-direction: column; align-items: center; justify-content: center;
    font-family: "Roboto Slab", serif; text-align: center; line-height: 1.1;
  }
  .offer .free { color: var(--orange); font-weight: 700; font-size: 30px; }
  .offer .word { color: var(--orange); font-weight: 700; font-size: 22px; }
  .offer .expires { font-size: 22px; }

  /* Info panel */
  .photo-round {
    position: absolute; left: 105px; top: 60px;
    width: 150px; height: 150px; border-radius: 50%;
    border: 6px solid var(--orange);
    background: radial-gradient(circle at 40% 40%, #cfe6f4, #6f9bc0 70%, #4b6d8e);
  }
  .info-title {
    position: absolute; left: 40px; top: 240px; width: 280px;
    font-family: "Roboto Slab", serif; font-weight: 700;
    font-size: 21px; line-height: 1.25; color: var(--blue); text-align: center;
  }
  .dots {
    position: absolute; left: 150px; top: 362px; width: 60px;
    border-top: 4px dotted var(--orange);
  }
  .info-body {
    position: absolute; left: 34px; top: 385px; width: 292px;
    font-size: 14px; line-height: 1.5; text-align: justify;
  }

  /* Cover panel */
  .cover-photo {
    position: absolute; left: 0; top: 90px; width: 100%; height: 230px;
    background: linear-gradient(135deg, #ffffff 0%, #eef2f5 45%, #e8d3c2 75%, #c9a88a 100%);
  }
  .quote {
    position: absolute; left: 195px; top: 210px;
    width: 145px; height: 145px; border-radius: 50%;
    background: var(--orange); border: 5px solid var(--white);
    display: flex; align-items: center; justify-content: center; text-align: center;
    font-family: "Roboto Slab", serif; font-weight: 700; font-size: 19px;
    color: var(--white); line-height: 1.2; padding: 12px;
  }
  .cover-lead {
    position: absolute; left: 30px; top: 362px; width: 300px;
    font-size: 20px; line-height: 1.25;
  }
  .cover-lead strong { font-weight: 700; }
  .questions {
    position: absolute; left: 30px; top: 455px; width: 300px;
    list-style: none;
  }
  .question {
    position: relative; padding-left: 22px; margin-bottom: 8px;
    font-size: 13px; line-height: 1.35; font-weight: 600;
  }
  .question::before {
    content: ""; position: absolute; left: 2px; top: 5px;
    width: 9px; height: 9px; border-radius: 50%;
    background: var(--orange);
  }
</style>
</head>
<body>
  <main class="brochure">
    <section class="panel panel-contact">
      <div class="header-band"><span class="brand">Bright Steps</span></div>
      <div class="contact">
        <div class="contact-icon">
          <svg width="26" height="26" viewBox="0 0 24 24" aria-hidden="true"><path fill="#fff" d="M6.6 10.8a15.1 15.1 0 0 0 6.6 6.6l2.2-2.2a1 1 0 0 1 1-.25 11.4 11.4 0 0 0 3.6.57 1 1 0 0 1 1 1V20a1 1 0 0 1-1 1A17 17 0 0 1 3 4a1 1 0 0 1 1-1h3.5a1 1 0 0 1 1 1c0 1.25.2 2.45.57 3.57a1 1 0 0 1-.25 1z"/></svg>
        </div>
        <p class="contact-line">(555)014-2290</p>
        <div class="contact-icon">@</div>
        <p class="contact-line email">BrightStepsOT@example.com</p>
        <p class="contact-name">Dana Levin OTR/L</p>
      </div>
      <div class="offer">
        <span class="free">FREE</span>
        <span class="word">evaluation</span>
        <span class="expires">offer expires</span>
        <span class="expires">07/02/15</span>
      </div>
      <div class="footer-band note">Only those that can benefit from this program will be accepted</div>
    </section>

    <section class="panel panel-info">
      <div class="header-band thin"></div>
      <div class="photo-round" role="img" aria-label="Photo of a young boy with glasses looking through a magnifying glass"></div>
      <h2 class="info-title">What is the benefit of having an OT work on Auditory processing skills?</h2>
      <div class="dots"></div>
      <p class="info-body">Hearing is connected to movement in the brain, when the proper movement is provided, the ears then open up to sounds and hearing. Movement is what OT's are skilled in providing. Therapies provided include movement, auditory processing, and visual processing techniques. Other techniques such as reflex integration may be incorporated.</p>
      <div class="footer-band claim">ONLY RESEARCHED BASED PROGRAMS USED</div>
    </section>

    <section class="panel panel-cover">
      <div class="header-band"><span class="brand">Bright Steps</span></div>
      <div class="cover-photo" role="img" aria-label="Photo of a smiling schoolgirl at a desk with sketched school doodles behind her"></div>
      <div class="quote">“Helping your child flourish”</div>
      <p class="cover-lead">Schools require <strong>great auditory</strong> and <strong>visual processing skills</strong></p>
      <ul class="questions">
        <li class="question">Does your child have difficulty learning the ABC and/or Aleph Bet?</li>
        <li class="question">Does your child know the material but still struggle on tests?</li>
        <li class="question">Does your child have trouble remembering names and dates at school, on tests or in daily life?</li>
      </ul>
      <div class="footer-band claim">YOUR CHILD CAN HAVE THESE SKILLS TOO!!</div>
    </section>
  </main>
</body>
</html>
```